Bamboo Wash Cloth Package Design

We need packaging designed for Bamboo Washcloths the Package will be: 25 cm x 14 cm x 4 cm
I am attaching Pictures of the box and our logo. All the language that is on the box will need to be on there, but can be moved and customized.
In addition to our logo the front of the box should have on it:
7 100% Natural Bamboo Washcloths
1 for Every Day of the Week
Ultra Soft
7 Pack of 10" by 10" Washcloths
Free from Chemicals, Toxins and Dyes
Perfect for Sensitive and Delicate Skin
Generously Sized
All Natural Bamboo
The Back should have our logo and the following language:
The Willow Nest Collection's premium 100% natural bamboo washcloths are the softest most gentle washcloths available. They are perfect for babies' delicate skin and for adults.
Willow Nest only uses the highest quality bamboo on the planet. Our perfectly sized washcloths are carefully woven into plush goodness featuring maximum absorbency and durability.
These eco-friendly washcloths, created from a sustainable source, are naturally antibacterial, hypoallergenic, and free from all dyes, chemicals, and toxins. They are comfort guaranteed and will leave you and your baby's skin feeling as pristine as nature intended.
The icons on the bottom of the box should also be used.
Additional thoughts:
1. Would like to see Bamboo and a Baby Panda worked into the design.
2.The Box can be 4 color.
3. I am attaching 3 box Pictures. The first 2 are picture of what our box is like for reference.
4. the 3rd is an idea of the color scheme I'd like to see utilized.
Please let me know if you have any questions.
Target Market(s)
Mothers and people who are environmentally conscious
Look and feel

```html
<!DOCTYPE html>
<html lang="en">
<head>
<meta charset="utf-8">
<title>Willow Nest Bamboo Washcloths – Package</title>
<link rel="stylesheet" href="https://fonts.googleapis.com/css2?family=Bree+Serif&family=Gochi+Hand&display=swap">
<style>
  :root {
    --stage: #eceef2;
    --kraft: #a98b63;
    --kraft-dark: #8f7350;
    --soil: #6b4423;
    --soil-dark: #55351a;
    --leaf: #4f7d32;
    --leaf-soft: #6f9a45;
    --ink: #2b2a38;
    --berry: #b3224f;
    --cream: #f4f2ea;
    --mint: #d8ecc7;
  }
  * { box-sizing: border-box; margin: 0; padding: 0; }
  html, body { width: 1200px; height: 632px; overflow: hidden; }
  body {
    background: linear-gradient(180deg, #d9dbe0 0%, var(--stage) 55%, #f7f7f9 100%);
    font-family: "Bree Serif", Georgia, serif;
    position: relative;
  }
  .panel {
    position: absolute;
    top: 160px;
    width: 560px;
    height: 314px;
    background: var(--kraft);
    overflow: hidden;
    box-shadow: 0 6px 18px rgba(0,0,0,.18);
  }
  .panel--front { left: 28px; }
  .panel--back { left: 612px; }

  .brand { position: absolute; left: 18px; top: 16px; width: 90px; text-align: center; }
  .brand__dot {
    display: block; width: 52px; height: 52px; margin: 0 auto 6px;
    border-radius: 50%; background: var(--leaf);
  }
  .brand__name { color: var(--leaf); font-size: 15px; line-height: 1; white-space: nowrap; }

  .count-badge {
    position: absolute; left: 108px; top: 20px; width: 38px; height: 38px;
    border-radius: 50%; background: var(--berry); color: #fff;
    font-size: 20px; line-height: 38px; text-align: center;
  }
  .title { position: absolute; left: 152px; top: 24px; color: var(--ink); font-size: 22px; white-space: nowrap; }
  .subtitle { position: absolute; left: 196px; top: 62px; color: var(--berry); font-size: 19px; white-space: nowrap; }

  .window {
    position: absolute; left: 82px; top: 102px; width: 318px; height: 128px;
    border-radius: 6px;
    background: linear-gradient(90deg, var(--mint) 0%, #cfe6bd 30%, var(--cream) 34%, #ece8dc 60%, var(--cream) 100%);
    box-shadow: inset 0 0 0 2px rgba(255,255,255,.5);
  }
  .art { position: absolute; border-radius: 4px; }
  .art--bamboo { background: linear-gradient(90deg, rgba(79,125,50,.55), rgba(111,154,69,.35)); }
  .art--panda { background: #cfc8bb; border-radius: 40%; }

  .features { position: absolute; left: 96px; top: 236px; display: flex; gap: 14px; z-index: 2; }
  .feature {
    width: 58px; height: 58px; border-radius: 50%; border: 3px solid var(--leaf);
    display: flex; align-items: center; justify-content: center; text-align: center;
    color: var(--ink); font-size: 8px; line-height: 1.15; padding: 4px;
  }
  .feature--lead { font-size: 12px; }

  .pack-sign {
    position: absolute; left: 438px; top: 184px; width: 90px; height: 62px;
    background: var(--soil-dark); color: #fff; border: 2px solid #8a6a4a;
    transform: rotate(-8deg); z-index: 2;
    font-family: "Gochi Hand", cursive; font-size: 14px; line-height: 1.05;
    display: flex; align-items: center; justify-content: center; text-align: center;
  }

  .ground { position: absolute; left: 0; bottom: 0; width: 100%; height: 52px; }

  .story-frame {
    position: absolute; left: 150px; top: 14px; width: 336px; height: 244px;
    border: 3px solid var(--leaf);
    padding: 14px 18px;
    color: var(--ink); font-size: 10.4px; line-height: 1.28; text-align: center;
  }
  .story-frame p + p { margin-top: 10px; }
  .story-frame .lead { color: var(--leaf); }
  .care { position: absolute; left: 150px; top: 264px; width: 340px; color: var(--ink); font-size: 7px; line-height: 1.3; z-index: 2; }
  .care-icons { display: flex; gap: 10px; margin-top: 4px; }
</style>
</head>
<body>

<section class="panel panel--front" aria-label="Front of box">
  <div class="brand"><span class="brand__dot"></span><span class="brand__name">willow nest</span></div>
  <div class="count-badge">7</div>
  <h1 class="title">100% Natural Bamboo Washcloths</h1>
  <h2 class="subtitle">1 for Every Day of the Week</h2>

  <div class="window" role="img" aria-label="Window showing seven folded washcloths, two pale green and the rest natural white"></div>

  <div class="art art--bamboo" style="left:12px;top:120px;width:50px;height:110px" role="img" aria-label="Bamboo stalks with leaves"></div>
  <div class="art art--panda" style="left:10px;top:208px;width:68px;height:78px" role="img" aria-label="Baby panda holding a bamboo sprig"></div>
  <div class="art art--bamboo" style="left:468px;top:92px;width:58px;height:200px" role="img" aria-label="Bamboo stalks with leaves"></div>

  <div class="pack-sign">7 Pack of<br>10 by 10<br>washcloths</div>

  <div class="features">
    <div class="feature feature--lead">Ultra Soft</div>
    <div class="feature">Free from Chemicals, Toxins and Dyes</div>
    <div class="feature">Perfect for Sensitive &amp; Delicate Skin</div>
    <div class="feature">Generously Sized</div>
    <div class="feature">All Natural Bamboo</div>
  </div>

  <svg class="ground" viewBox="0 0 560 52" preserveAspectRatio="none" aria-hidden="true">
    <path d="M0 30 C120 14 260 20 380 30 S520 40 560 22 L560 52 L0 52 Z" fill="var(--soil)"/>
  </svg>
</section>

<section class="panel panel--back" aria-label="Back of box">
  <div class="brand"><span class="brand__dot"></span><span class="brand__name">willow nest</span></div>

  <div class="art art--bamboo" style="left:22px;top:110px;width:50px;height:120px" role="img" aria-label="Bamboo stalks with leaves"></div>
  <div class="art art--panda" style="left:20px;top:210px;width:66px;height:76px" role="img" aria-label="Baby panda holding a bamboo sprig"></div>

  <div class="story-frame">
    <p><span class="lead">The Willow Nest Collection's</span> premium 100% natural bamboo washcloths are the softest most gentle washcloths available. They are perfect for babies' delicate skin and for adults.</p>
    <p>Willow Nest only uses the highest quality bamboo on the planet. Our perfectly sized washcloths are carefully woven into plush goodness featuring maximum absorbency and durability.</p>
    <p>These eco-friendly washcloths, created from a sustainable source, are naturally antibacterial, hypoallergenic, and free from all dyes, chemicals, and toxins. They are comfort guaranteed and will leave you and your baby's skin feeling as pristine as nature intended.</p>
  </div>

  <div class="care">
    Care Instruction: Wash before use. Machine wash cold with like colors.<br>
    Do not use bleach. Tumble dry low. Do not iron.
    <div class="care-icons" aria-label="Care symbols">
      <svg width="16" height="12" viewBox="0 0 16 12"><path d="M1 2 L3 11 H13 L15 2" fill="none" stroke="var(--ink)"/><text x="8" y="9" font-size="5" text-anchor="middle" fill="var(--ink)">30</text></svg>
      <svg width="16" height="12" viewBox="0 0 16 12"><path d="M8 1 L15 11 H1 Z M3 2 L13 11 M13 2 L3 11" fill="none" stroke="var(--ink)"/></svg>
      <svg width="14" height="12" viewBox="0 0 14 12"><rect x="1" y="1" width="12" height="10" fill="none" stroke="var(--ink)"/><circle cx="7" cy="6" r="3.5" fill="none" stroke="var(--ink)"/><circle cx="7" cy="6" r=".8" fill="var(--ink)"/></svg>
      <svg width="16" height="12" viewBox="0 0 16 12"><path d="M2 10 H14 L12 4 H5 Q3 4 2 10 Z M2 1 L14 11 M14 1 L2 11" fill="none" stroke="var(--ink)"/></svg>
    </div>
  </div>

  <svg class="ground" viewBox="0 0 560 52" preserveAspectRatio="none" aria-hidden="true">
    <path d="M0 36 C140 24 300 30 420 38 S530 44 560 32 L560 52 L0 52 Z" fill="var(--soil)"/>
  </svg>
</section>

</body>
</html>
```